Create the BEST and COOLEST website for events and media company!

Hi there. I am a start-up events and conferences company with a twist, and we are seeking a highly modern website for our company Quillfern Media. Our company believes that (like the social networking theory) that each and every one of us is connected to anyone on the planet in six connections or less. E.g. I know someone, who knows someone, who knows someone. Hence, the name Quillfern Media.

I have included the copy for the website attached.

While we do have a business audience, they are in the fields of technology from the banking, health, government sector. We would like our website to be edgy, fresh and steer away from stuffy corporate images.

To give you an idea, our website menu tabs will be labelled:
HOME: This will include a corporate video that’s being created next week for me. However, please still design this page with a very striking background image that fills the whole page. You can run the copy and put a mock video for me to just see the layout (we can insert the finished video later).

ROCKSTARS: this will show pictures of highly powerful leaders speaking on stage; with a highly engaged audience watching. We want to show we have the world’s best technology International speakers “rockstars” who are the best in their game when it comes to talking about the future of technology.

LOCAL LEGENDS: like the international ‘rockstar’ speakers we would bring over to Australia to present; this LOCAL LEGENDS page should show we have the best home-grown Chief business people speaking at conferences and smaller powerful roundtable luncheons.

UNSUNG HEROES: this is more the people in the audience who ask questions on a microphone; those that attend the conferences; or a speaking to people at a conference.

THE BAND: this is like an ‘about us’ – just a funkier name to tie in with the theme of rockstars, etc.

THE PARTNERS: this is like a sponsor client page, where we invite people to partner with us and sponsor our events and conferences.

YOU & DORIAN PELLHAM: Dorian Pellham is a famous actor who made the term ‘six degrees of separation’ very popular. This page will have a little bit of an introduction, but mainly have the following video fill the landing page: https://www.vidplume.example/watch?v=Tq4-zLp8XwE

Website Functionality and Features:

• Try and make the ‘vibe’ and look and feel consistent, hip and modern (but still maintain a professional look). At the end of the day, people looking at our website are very senior business chiefs of organisations and also marketing chiefs.
• We may add more pages once we become established, so the website needs to ensure we can do that easily.
• We want pictures to not look stock photos. We want them to fresh, innovative, inspirational.
• Images should have a ‘wow’ factor. Like this one: https://www.picharbor.example/detail/news-photo/general-view-of-atmosphere-during-brightloom-talks-2018-from-me-news-photo/481253907
• Need a mix of speaker, stage, audience, pictures. While we want to be fresh, edgy and contemporary we need to remember our viewers are the big chiefs of businesses – so lets try and have cool shots, but ensure there is a link to the business decision makers in a modern way. They all don’t have to wear suits, but not too casual either
• Other types of imagery I like is this one: https://www.picharbor.example/detail/photo/smiling-audience-using-smart-phone-flashlights-for-royalty-free-image/362817045.
• The following are ok, not wow – but to give you an idea:
• https://www.picharbor.example/detail/photo/smiling-male-speaker-in-wheelchair-on-stage-royalty-free-image/362819531
https://www.picharbor.example/detail/photo/smiling-woman-with-camera-phone-in-dark-audience-royalty-free-image/362818476
https://www.picharbor.example/detail/photo/audience-using-camera-phones-royalty-free-image/367402158
https://www.picharbor.example/detail/photo/male-speaker-on-stage-talking-to-audience-royalty-free-image/362818893

NB: Logos are supplied in low resolution, but I can send you high resolution also
Updates

Hi there I will be adding two low-resolution images of my business partner and I for the ABOUT US page which is called THE BAND in the menu tab.

Hi everyone, thank you for your designs. I have uploaded a MAIN SCREEN IDEAS word document to give you further ideas of how the options I like for the main landing page on the home page. Hope this helps!

Target Market(s)

High end business people in marketing and business.

Coding

Coded - Design and coding required

Number of Pages Required

5+ page

Font styles to use
Sans Serif

Requirements
Must have
• Fresh, inspirational and aspirational designs. We need to make events and conferences look exciting and that we are bring the best technology speakers (like Brightloom events) to our audience of marketing and technology professionals.
Should not have
• Cheesy, old stock photos; or pictures of American executives as this is for an Australian audience.
• PLEASE do not include an UPCOMING EVENTS or a SPEAKERS section as we will not be having this showcasing. You can feature ROCK STARS, LOCAL LEGENDS and UNSUNG HEROES if you like on the home page + the video of YOU and DORIAN PELLHAM (with his picture on the video box with a play button)

```html
<!DOCTYPE html>
<html lang="en">
<head>
<meta charset="utf-8">
<title>Quillfern Media — Events &amp; Conferences</title>
<link href="https://fonts.googleapis.com/css2?family=Lato:wght@400;700;900&family=Roboto:wght@400;500&display=swap" rel="stylesheet">
<style>
:root{
  --blue:#1a7fd6;
  --blue-bright:#2190e8;
  --navy:#1b3a8f;
  --navy-deep:#142c70;
  --ink:#111111;
  --text:#555b63;
  --label:#1f3c99;
  --light:#f1f2f4;
  --footer:#1d1d1f;
  --white:#ffffff;
}
*{margin:0;padding:0;box-sizing:border-box}
html,body{width:1200px;height:4018px;overflow:hidden}
body{position:relative;font-family:"Roboto",Arial,sans-serif;color:var(--text);background:var(--white)}
.abs{position:absolute}
.heading{font-family:"Lato",Arial,sans-serif;font-weight:900;color:var(--ink);text-transform:uppercase}
.label{font-family:"Lato",Arial,sans-serif;font-weight:700;font-size:18px;letter-spacing:2px;color:var(--label);text-transform:uppercase}
.center{left:0;width:1200px;text-align:center}
.btn{display:flex;align-items:center;justify-content:center;gap:8px;border-radius:30px;font-family:"Lato",Arial,sans-serif;font-weight:700;font-size:14px;text-transform:uppercase;color:var(--white)}

/* hero */
.hero{top:0;left:0;width:1200px;height:683px;background:radial-gradient(ellipse at 30% 40%,#3a4a62 0%,#1c2433 45%,#0b0f17 100%)}
.brand{top:28px;left:0;width:1200px;text-align:center;color:var(--white)}
.brand-mark{width:34px;height:34px;border:3px solid var(--white);border-radius:50%;margin:0 auto 6px}
.brand-name{font-family:"Lato",sans-serif;font-weight:900;font-size:20px;letter-spacing:1px;text-transform:uppercase}
.brand-tag{font-size:10px;letter-spacing:3px;margin-top:2px}
.nav-rule{top:118px;left:112px;width:976px;height:1px;background:rgba(255,255,255,.35)}
.nav{top:138px;left:112px;width:976px;display:flex;justify-content:space-between;list-style:none}
.nav li{font-family:"Lato",sans-serif;font-weight:700;font-size:16px;color:var(--white);text-transform:uppercase}
.hero-play{top:290px;left:668px}
.hero-title{top:372px;left:668px;font-family:"Lato",sans-serif;font-weight:900;font-size:60px;line-height:68px;color:var(--white);text-transform:uppercase;letter-spacing:1px}

/* join band */
.join{top:683px;left:0;width:1200px;height:207px;background:linear-gradient(90deg,var(--blue) 0%,var(--blue-bright) 60%,#1a7fd6 100%)}
.join h2{top:738px;left:112px;font-family:"Lato",sans-serif;font-weight:900;font-size:34px;color:var(--white)}
.join-rule{top:788px;left:112px;width:66px;height:3px;background:var(--white)}
.join p{top:804px;left:112px;font-size:15px;color:rgba(255,255,255,.9)}
.join .btn{top:763px;left:895px;width:193px;height:44px;background:var(--navy);font-size:15px}

/* about */
.about-label{top:1004px;left:112px}
.about-title{top:1034px;left:112px;font-size:38px}
.about-rule{top:1084px;left:112px;width:66px;height:3px;background:var(--blue)}
.about-copy{top:1112px;left:112px;width:460px;font-size:13.5px;line-height:25px}
.about .btn{top:1283px;left:112px;width:252px;height:44px;background:var(--blue)}
.about-photo{top:1012px;left:640px;width:448px;height:285px;background:linear-gradient(135deg,#27315a 0%,#121a33 55%,#3d2f2a 100%)}
.about-play{top:1263px;left:604px}

/* speakers */
.speakers{top:1441px;left:0;width:1200px;height:574px;background:linear-gradient(180deg,var(--navy) 0%,var(--navy-deep) 100%)}
.speakers .label{top:1524px;color:rgba(255,255,255,.85)}
.speakers-title{top:1554px;font-size:36px;color:var(--white)}
.speakers-intro{top:1608px;font-size:15px;color:rgba(255,255,255,.9)}
.speaker{top:1671px;width:210px;text-align:center}
.speaker-photo{width:210px;height:210px;border-radius:50%;background:radial-gradient(circle at 50% 40%,#c9a48a 0%,#7b5a4a 40%,#2f2a2b 100%)}
.speaker-photo.overlay{background:var(--blue-bright);display:flex;align-items:center;justify-content:center;gap:12px}
.speaker-photo.overlay span{width:22px;height:22px;border-radius:50%;background:var(--white)}
.speaker-name{margin-top:20px;font-family:"Lato",sans-serif;font-weight:700;font-size:26px;color:var(--white)}

/* events */
.events .label{top:2105px}
.events-title{top:2130px;font-size:38px}
.events-intro{top:2196px;font-size:15px}
.event-card{top:2250px;width:299px;height:295px;overflow:hidden;background:linear-gradient(150deg,#6d4b3a 0%,#2d3a55 60%,#1a2238 100%)}
.event-card svg{position:absolute;left:0;bottom:0}
.event-name{position:absolute;left:18px;bottom:18px;font-family:"Lato",sans-serif;font-weight:900;font-size:20px;color:var(--white)}
.event-arrow{position:absolute;right:18px;bottom:20px}
.event-card.active .event-name{bottom:auto;top:194px}
.event-text{position:absolute;left:18px;top:230px;width:250px;font-size:13px;line-height:20px;color:var(--white)}
.view-all{top:2604px;left:493px;width:214px;height:48px;border:2px solid #d8dce2;color:var(--label);font-size:15px}

/* partners */
.partners{top:2760px;left:0;width:1200px;height:423px;background:linear-gradient(180deg,#f6f6f7 0%,#e9eaec 100%)}
.partners .label{top:2877px}
.partners-title{top:2902px;font-size:38px}
.partner{top:2990px;width:182px;height:80px;background:var(--white);display:flex;align-items:center;justify-content:center;box-shadow:0 2px 8px rgba(0,0,0,.06)}
.partner span{width:120px;height:26px;border-radius:4px;background:#c9ccd1}
.slider-arrow{top:3018px}

/* call to action */
.cta{top:3183px;left:0;width:1200px;height:385px;background:linear-gradient(90deg,#1a6fd0 0%,var(--blue-bright) 50%,#1a6fd0 100%)}
.cta-kicker{top:3263px;font-family:"Lato",sans-serif;font-weight:700;font-size:18px;letter-spacing:2px;color:var(--white)}
.cta-title{top:3292px;font-size:38px;color:var(--white)}
.cta-sub{top:3356px;font-family:"Lato",sans-serif;font-weight:700;font-size:22px;letter-spacing:1px;color:var(--white)}
.cta-icon{top:3424px;left:568px}

/* footer */
.footer{top:3568px;left:0;width:1200px;height:450px;background:var(--footer)}
.f-head{top:3668px;font-family:"Lato",sans-serif;font-weight:900;font-size:19px;color:var(--white);text-transform:uppercase}
.f-links{top:3708px;left:112px;list-style:none}
.f-links li{font-size:14px;line-height:27px;color:#d7d7d7;display:flex;align-items:center;gap:10px}
.f-links li::before{content:"";width:0;height:0;border-left:6px solid #d7d7d7;border-top:4px solid transparent;border-bottom:4px solid transparent}
.f-contact{left:424px;display:flex;gap:28px;font-size:14px;line-height:22px;color:#d7d7d7}
.f-contact svg{flex:none;margin-top:2px}
.f-news{top:3706px;left:833px;width:260px;font-size:14px;line-height:22px;color:#d7d7d7}
.f-input{top:3773px;left:833px;width:255px;height:36px;border:1px solid #8a8a8a;font-size:12px;color:#d7d7d7;padding:10px 12px}
.f-sub{top:3828px;left:833px;width:100px;height:32px;background:var(--blue);font-size:12px}
.f-rule{top:3925px;left:112px;width:976px;height:1px;background:#444}
.copyright{top:3960px;left:112px;font-size:14px;color:#d7d7d7}
.f-social{top:3954px;left:956px;display:flex;gap:8px}
.f-social span{width:28px;height:28px;border:1.5px solid #d7d7d7;border-radius:50%}
</style>
</head>
<body>

<!-- hero -->
<section class="abs hero" role="img" aria-label="Speaker in white shirt on stage facing a large conference audience"></section>
<div class="abs brand">
  <div class="brand-mark"></div>
  <div class="brand-name">Quillfern Media</div>
  <div class="brand-tag">WHERE LEADERS CONNECT</div>
</div>
<div class="abs nav-rule"></div>
<ul class="abs nav">
  <li>Home</li><li>Rockstars</li><li>Local Legends</li><li>Unsung Heroes</li><li>The Band</li><li>The Partners</li><li>You &amp; Dorian Pellham</li>
</ul>
<svg class="abs hero-play" width="64" height="64" viewBox="0 0 64 64"><circle cx="32" cy="32" r="32" fill="#1a7fd6"/><path d="M25 20 L46 32 L25 44 Z" fill="#fff"/></svg>
<h1 class="abs hero-title">Events &amp;<br>Conferences</h1>

<!-- join -->
<section class="abs join" role="img" aria-label="Blue tinted audience backdrop"></section>
<h2 class="abs" style="top:738px;left:112px;font-family:'Lato',sans-serif;font-weight:900;font-size:34px;color:#fff">ARE YOU READY JOING US?</h2>
<div class="abs join-rule"></div>
<p class="abs" style="top:804px;left:112px;font-size:15px;color:rgba(255,255,255,.9)">Sed egestas, ante et vulputate volutpat, eros pede semper est, vitae luctus metus libero eu augue.</p>
<div class="abs btn" style="top:763px;left:895px;width:193px;height:44px;background:var(--navy);font-size:15px">Register Today
  <svg width="14" height="14" viewBox="0 0 14 14"><circle cx="7" cy="7" r="7" fill="#fff"/><path d="M5.5 4 L9 7 L5.5 10" stroke="#1b3a8f" stroke-width="1.8" fill="none"/></svg></div>

<!-- about -->
<section class="about">
  <div class="abs label about-label">Greetings &amp; Welcome</div>
  <h2 class="abs heading about-title">About Quillfern Media</h2>
  <div class="abs about-rule"></div>
  <p class="abs about-copy">Lorem ipsum dolor sit amet, consectetur adipiscing elit, sed do eiusmod tempor incididunt ut labore et dolore magna aliqua. Ut enim ad minim veniam, quis nos trud exercitation ullamco laboris nisi ut aliquip ex ea commodo consequat. Duis aute irure dolor in reprehenderit in voluptate velit esse cillum dolore eu fugiat nulla pariatur.</p>
  <div class="abs btn">Business Decision Makers</div>
  <div class="abs about-photo" role="img" aria-label="Speaker on a lit stage with audience in the foreground"></div>
  <svg class="abs about-play" width="70" height="70" viewBox="0 0 70 70"><circle cx="35" cy="35" r="33" fill="#fff" stroke="#1a7fd6" stroke-width="3"/><path d="M28 23 L48 35 L28 47 Z" fill="#1a7fd6"/></svg>
</section>

<!-- speakers -->
<section class="abs speakers" role="img" aria-label="Navy tinted stage backdrop"></section>
<div class="abs label center" style="top:1524px;color:rgba(255,255,255,.85)">Rockstars</div>
<h2 class="abs heading center speakers-title">Event Speakers</h2>
<p class="abs center speakers-intro">Lorem ipsum dolor sit amet, consectetur adipiscing incididunt ut labore et dolore magna aliqua.</p>
<div class="abs speaker" style="left:112px"><div class="speaker-photo" role="img" aria-label="Portrait of speaker Ayrin Dina"></div><div class="speaker-name">Ayrin Dina</div></div>
<div class="abs speaker" style="left:367px"><div class="speaker-photo overlay" role="img" aria-label="Portrait of speaker Cristian Zozo with social links overlay"><span></span><span></span><span></span><span></span></div><div class="speaker-name">Cristian Zozo</div></div>
<div class="abs speaker" style="left:624px"><div class="speaker-photo" role="img" aria-label="Portrait of speaker James Morgan"></div><div class="speaker-name">James Morgan</div></div>
<div class="abs speaker" style="left:878px"><div class="speaker-photo" role="img" aria-label="Portrait of speaker Mark Willy"></div><div class="speaker-name">Mark Willy</div></div>

<!-- events -->
<section class="events">
  <div class="abs label center">Performers</div>
  <h2 class="abs heading center events-title">Upcoming Events</h2>
  <p class="abs center events-intro">Lorem ipsum dolor sit amet consectetur adipiscing ellit incididunt ut labore et dolore magna aliqua.</p>

  <div class="abs event-card" style="left:112px" role="img" aria-label="Roundtable meeting in a conference hall">
    <svg width="299" height="80" viewBox="0 0 299 80"><path d="M0 20 L299 0 L299 80 L0 80 Z" fill="#1b3a8f" opacity=".92"/></svg>
    <div class="event-name">EVENT NAME</div>
    <svg class="event-arrow" width="18" height="18" viewBox="0 0 18 18"><circle cx="9" cy="9" r="9" fill="#fff"/><path d="M7 5 L11 9 L7 13" stroke="#1b3a8f" stroke-width="2" fill="none"/></svg>
  </div>
  <div class="abs event-card active" style="left:450px" role="img" aria-label="Speaker addressing a crowd on a blue lit stage">
    <svg width="299" height="135" viewBox="0 0 299 135"><path d="M0 20 L299 0 L299 135 L0 135 Z" fill="#2190e8" opacity=".95"/></svg>
    <div class="event-name">EVENT NAME</div>
    <p class="event-text">Lorem ipsum dolor sit amet consectetur adipiscing tempor incididunt...</p>
    <svg class="event-arrow" width="18" height="18" viewBox="0 0 18 18"><circle cx="9" cy="9" r="9" fill="#fff"/><path d="M7 5 L11 9 L7 13" stroke="#2190e8" stroke-width="2" fill="none"/></svg>
  </div>
  <div class="abs event-card" style="left:788px" role="img" aria-label="Presenter on stage viewed from the audience">
    <svg width="300" height="80" viewBox="0 0 300 80"><path d="M0 20 L300 0 L300 80 L0 80 Z" fill="#1b3a8f" opacity=".92"/></svg>
    <div class="event-name">EVENT NAME</div>
    <svg class="event-arrow" width="18" height="18" viewBox="0 0 18 18"><circle cx="9" cy="9" r="9" fill="#fff"/><path d="M7 5 L11 9 L7 13" stroke="#1b3a8f" stroke-width="2" fill="none"/></svg>
  </div>
  <div class="abs btn view-all">View All Events
    <svg width="14" height="14" viewBox="0 0 14 14"><circle cx="7" cy="7" r="7" fill="#1f3c99"/><path d="M5.5 4 L9 7 L5.5 10" stroke="#fff" stroke-width="1.8" fill="none"/></svg></div>
</section>

<!-- partners -->
<section class="abs partners" role="img" aria-label="Soft grey backdrop with a microphone on stage"></section>
<svg class="abs" style="top:2760px;left:0" width="1200" height="80" viewBox="0 0 1200 80"><path d="M0 0 L1200 0 L1200 70 Q600 -50 0 70 Z" fill="#fff"/></svg>
<div class="abs label center" style="top:2877px">Sponsor</div>
<h2 class="abs heading center partners-title">Our Partners</h2>
<div class="abs partner" style="left:112px" aria-label="Partner badge"><span></span></div>
<div class="abs partner" style="left:311px" aria-label="Partner badge"><span></span></div>
<div class="abs partner" style="left:509px" aria-label="Partner badge"><span></span></div>
<div class="abs partner" style="left:707px" aria-label="Partner badge"><span></span></div>
<div class="abs partner" style="left:906px" aria-label="Partner badge"><span></span></div>
<svg class="abs slider-arrow" style="left:55px" width="16" height="26" viewBox="0 0 16 26"><path d="M13 2 L3 13 L13 24" stroke="#666" stroke-width="3" fill="none"/></svg>
<svg class="abs slider-arrow" style="left:1128px" width="16" height="26" viewBox="0 0 16 26"><path d="M3 2 L13 13 L3 24" stroke="#666" stroke-width="3" fill="none"/></svg>

<!-- call to action -->
<section class="abs cta" role="img" aria-label="Blue tinted photo of a woman speaking at an event"></section>
<div class="abs center cta-kicker">ALWAYS LIVE WITH WORLD</div>
<h2 class="abs heading center cta-title">Don’t Forget This Event To Attend,</h2>
<div class="abs center cta-sub">ADD TO YOUR CALENDAR NOW!</div>
<svg class="abs cta-icon" width="64" height="64" viewBox="0 0 64 64"><circle cx="32" cy="32" r="32" fill="#fff"/><rect x="21" y="23" width="22" height="20" rx="2" fill="none" stroke="#1a7fd6" stroke-width="2.5"/><path d="M21 29 H43 M26 19 V26 M38 19 V26" stroke="#1a7fd6" stroke-width="2.5"/><path d="M26 34 H29 M31 34 H34 M36 34 H39 M26 38 H29 M31 38 H34" stroke="#1a7fd6" stroke-width="2"/></svg>

<!-- footer -->
<footer class="abs footer"></footer>
<div class="abs f-head" style="left:112px">Quick Links</div>
<ul class="abs f-links">
  <li>Home</li><li>Rockstars</li><li>Local Legends</li><li>The Band</li><li>The Partners</li><li>You &amp; Dorian Pellham</li>
</ul>
<div class="abs f-head" style="left:424px">Contact Details</div>
<div class="abs f-contact" style="top:3713px">
  <svg width="14" height="18" viewBox="0 0 14 18"><path d="M7 1 C3.5 1 1 3.6 1 7 C1 11 7 17 7 17 C7 17 13 11 13 7 C13 3.6 10.5 1 7 1 Z" fill="none" stroke="#bbb" stroke-width="1.5"/><circle cx="7" cy="7" r="2" fill="#bbb"/></svg>
  <div>123A, Sample Street, Sample City,<br>New State. PO 1234</div>
</div>
<div class="abs f-contact" style="top:3781px">
  <svg width="16" height="16" viewBox="0 0 16 16"><path d="M3 1 L6 1 L7 5 L5 6.5 C6 9 7 10 9.5 11 L11 9 L15 10 L15 13 C15 14 14 15 13 15 C6.5 14.5 1.5 9.5 1 3 C1 2 2 1 3 1 Z" fill="none" stroke="#bbb" stroke-width="1.4"/></svg>
  <div>(+1) 123 456 7890</div>
</div>
<div class="abs f-contact" style="top:3840px">
  <svg width="16" height="14" viewBox="0 0 16 14"><rect x="1" y="2" width="14" height="10" fill="none" stroke="#bbb" stroke-width="1.4"/><path d="M1 2 L8 8 L15 2" fill="none" stroke="#bbb" stroke-width="1.4"/></svg>
  <div>hello@quillfernmedia.com</div>
</div>
<div class="abs f-head" style="left:833px">Newsletter Subscription</div>
<p class="abs f-news">Register your Email Address to get More Information about us</p>
<div class="abs f-input">Email Address</div>
<div class="abs btn f-sub">Subscribe</div>
<div class="abs f-rule"></div>
<div class="abs copyright">Copyrights © 2019 Quillfern Media  All Rights Reserved.</div>
<div class="abs f-social"><span></span><span></span><span></span><span></span></div>

</body>
</html>
```